Need a book cover design for a Lumora Book

Book has a long title and sub title so lots of words to fit on the cover.

I can be flexible a bit with the sub title due to the length of it but ideally i can get a design that takes everything.

Here is the title:

Tidal Geology: The Roots of Erosion, Sedimentation, and Canyon Forming

Sub Title/Heading
An Easy Primer on Coastal Cliffs, Dune Drift, River Beds, and Delta Mapping Methods

```html
<!DOCTYPE html>
<html lang="en">
<head>
<meta charset="utf-8">
<title>Tidal Geology — Lumora Book Cover</title>
<link rel="stylesheet" href="https://fonts.googleapis.com/css2?family=Arimo:wght@700&family=EB+Garamond:ital@1&display=swap">
<style>
  :root {
    --navy: #030822;
    --navy-mid: #0a1a45;
    --tagline: #9fd3ee;
    --white: #ffffff;
    --glow-core: #e9ffff;
    --glow-cyan: #2fd6e6;
    --glow-teal: #0d6f9a;
  }
  * { margin: 0; padding: 0; box-sizing: border-box; }
  html, body {
    width: 840px;
    height: 1200px;
    overflow: hidden;
    background: var(--navy);
  }
  .cover {
    position: relative;
    width: 840px;
    height: 1200px;
    background: radial-gradient(ellipse at 50% 45%, var(--navy-mid) 0%, var(--navy) 70%);
    overflow: hidden;
    text-align: center;
    color: var(--white);
  }
  .tagline {
    position: absolute;
    top: 44px;
    left: 60px;
    right: 60px;
    font-family: "EB Garamond", serif;
    font-style: italic;
    font-size: 21px;
    line-height: 24px;
    color: var(--tagline);
  }
  .title {
    position: absolute;
    top: 170px;
    left: 0;
    right: 0;
    font-family: "Arimo", Arial, sans-serif;
    font-weight: 700;
    font-size: 136px;
    line-height: 118px;
    letter-spacing: -1px;
    color: var(--white);
  }
  .subtitle {
    position: absolute;
    top: 448px;
    left: 30px;
    right: 30px;
    font-family: "Arimo", Arial, sans-serif;
    font-weight: 700;
    font-size: 27px;
    line-height: 34px;
    color: var(--white);
  }
  .artwork {
    position: absolute;
    left: 120px;
    top: 540px;
    width: 580px;
    height: 560px;
    background: radial-gradient(circle at 50% 52%,
      var(--glow-core) 0%,
      var(--glow-cyan) 7%,
      rgba(13, 111, 154, 0.55) 22%,
      rgba(10, 26, 69, 0.3) 45%,
      rgba(3, 8, 34, 0) 70%);
  }
</style>
</head>
<body>
  <main class="cover">
    <p class="tagline">An Easy Primer on Coastal Cliffs, Dune Drift, River Beds,<br>and Delta Mapping Methods</p>
    <h1 class="title">TIDAL<br>GEOLOGY</h1>
    <h2 class="subtitle">THE ROOTS OF EROSION, SEDIMENTATION,<br>AND CANYON FORMING</h2>
    <div class="artwork" role="img" aria-label="Glowing cyan illustration with light streaks and orbiting trails on a dark navy background"></div>
  </main>
</body>
</html>
```